Flyer für Fußball-Förderverein
Zielgruppe
Wir sind der Fußball-Förderverein des SpVg Halmbeck.
Aufgabenstellung
1. Ziel des Flyers:
Der Flyer soll den Förderverein des SpVg Halmbeck bekannter machen und neue Mitglieder und Sponsoren gewinnen. Er soll darüber informieren, wie der Förderverein den Verein unterstützt und warum eine Mitgliedschaft oder eine Spende wichtig ist.
2. Zielgruppe:
Eltern der Kinder und Jugendlichen, die im SpVg Halmbeck Fußball spielen.
Lokale Unternehmen und potenzielle Sponsoren.
Vereinsmitglieder und Fußballinteressierte in der Region.
3. Hauptbotschaft:
„Unterstütze den SpVg Halmbeck – Gemeinsam für die Zukunft unseres Vereins und der Jugend!“
4. Inhalte:
Über den Förderverein:
Eine kurze Beschreibung des Fördervereins, warum er existiert und was er für den Verein und die Jugend tut.
Mitgliedschaft:
Informationen, wie man Mitglied im Förderverein werden kann. Vorteile und der Beitrag, der benötigt wird.
Spenden:
Möglichkeit der direkten Spende mit einem Hinweis auf steuerliche Vorteile (falls zutreffend). Möglicherweise auch die Angabe eines Spendenkontos.
Beispiele für die Verwendung von Mitteln:
Welche Projekte oder Anschaffungen wurden durch den Förderverein unterstützt (z.B. Trainingsmaterialien, Ausrüstung, Turniere, Jugendfahrten)?
Kontaktinformationen:
Ansprechpartner des Fördervereins mit Telefonnummer, E-Mail-Adresse und eventuell ein Link zur Webseite oder Social-Media-Profilen.
5. Designvorgaben:
Farben und Stil:
Die Vereinsfarben des SpVg Halmbeck sollten im Flyer dominieren (grün-weiß, etc.). Ein modernes, aber sportliches Design, das dynamisch wirkt und die Zielgruppe anspricht.
Logo:
Das Logo des SpVg Halmbeck sollte prominent platziert werden, ebenso das Logo des Fördervereins (falls vorhanden).
Bilder:
Verwendung von Bildern aus dem Vereinsleben, insbesondere von Kindern und Jugendlichen im Spielbetrieb oder bei Vereinsaktivitäten. Falls keine spezifischen Bilder vorhanden sind, können allgemeine Fußballbilde..

```html
<!DOCTYPE html>
<html lang="de">
<head>
<meta charset="utf-8">
<title>Flyer Förderverein SpVg Halmbeck</title>
<link href="https://fonts.googleapis.com/css2?family=Montserrat:wght@400;500;600;700;800&family=Oswald:wght@700&display=swap" rel="stylesheet">
<style>
  :root{
    --green:#17963b;
    --green-dark:#0f7a2d;
    --green-light:#22ab47;
    --grass:#4f8f2c;
    --ink:#111111;
    --white:#ffffff;
    --stage:#c9c9c9;
  }
  *{box-sizing:border-box;margin:0;padding:0}
  html,body{width:889px;height:1200px;overflow:hidden}
  body{background:var(--stage);font-family:"Montserrat",sans-serif;position:relative}
  .page{position:absolute;top:317px;width:400px;height:566px;overflow:hidden;box-shadow:0 6px 18px rgba(0,0,0,.25)}
  .page--front{left:30px;background:var(--white)}
  .page--back{left:459px;background:linear-gradient(160deg,var(--green-light),var(--green) 45%,var(--green-dark))}
  .shapes{position:absolute;inset:0;width:400px;height:566px}
  .abs{position:absolute}

  .club-mark{display:flex;flex-direction:column;align-items:center;justify-content:center;gap:10px;text-align:center}
  .club-mark__dot{width:62px;height:62px;border-radius:50%;background:var(--ink)}
  .club-mark__name{font-weight:800;font-size:9.5px;line-height:1.3;letter-spacing:.2px;text-transform:uppercase;white-space:nowrap}
  .page--front .club-mark__name{color:var(--ink)}
  .page--back .club-mark__name{color:var(--white)}

  .headline{left:27px;top:212px;font-family:"Oswald",sans-serif;font-weight:700;font-size:35px;line-height:.98;color:var(--white);letter-spacing:-.5px;white-space:nowrap}
  .tagline{left:29px;top:296px;width:150px;font-weight:600;font-size:10.5px;line-height:1.15;color:var(--white);white-space:nowrap}

  .info-box{left:17px;top:384px;width:364px;height:134px;border:1.5px solid var(--green);background:var(--white);display:flex;padding:12px 14px 10px 16px}
  .info-box__col{flex:1}
  .info-box__col--left{padding-right:12px;border-right:1px solid #d9d9d9}
  .info-box__col--right{padding-left:12px}
  .info-box h2{font-weight:800;font-size:14.5px;line-height:1.05;color:var(--green);text-transform:uppercase}
  .info-box h3{font-weight:700;font-size:9.5px;line-height:1.2;color:var(--green)}
  .info-box p{font-size:5.6px;line-height:1.3;color:#333;margin-top:8px}
  .website{left:0;width:330px;top:532px;text-align:center;font-weight:800;font-size:12px;color:var(--green)}

  .back-section h2{font-weight:800;font-size:10.5px;line-height:1.1;color:var(--white);text-transform:uppercase;padding-bottom:5px;border-bottom:1px solid rgba(255,255,255,.8);margin-bottom:6px}
  .back-section p{font-size:5.8px;line-height:1.28;color:var(--white)}
  .membership{left:32px;top:22px;width:148px}
  .donations{left:212px;top:19px;width:170px;height:72px;border:1.5px solid var(--white);padding:10px 10px}
  .benefits{left:19px;top:112px;width:175px;height:200px;border:1.5px solid var(--white);border-bottom:none;padding:10px 12px}
  .examples{left:226px;top:106px;width:150px}

  .contact{left:34px;top:486px;list-style:none;color:var(--white);font-weight:700;font-size:11px;line-height:1.45}
  .contact li{display:flex;align-items:center;gap:4px}
  .contact svg{width:9px;height:9px;flex:none}
</style>
</head>
<body>

<!-- Vorderseite -->
<section class="page page--front">
  <svg class="shapes" viewBox="0 0 400 566">
    <defs>
      <linearGradient id="kidsPhoto" x1="0" y1="0" x2="0" y2="1">
        <stop offset="0" stop-color="#5f8d46"/>
        <stop offset=".45" stop-color="#2ea04a"/>
        <stop offset="1" stop-color="#4c8a2a"/>
      </linearGradient>
      <linearGradient id="drillPhoto" x1="0" y1="0" x2="0" y2="1">
        <stop offset="0" stop-color="#7aa75a"/>
        <stop offset="1" stop-color="#3f7f25"/>
      </linearGradient>
    </defs>
    <polygon points="0,181 400,88 400,294 72,369 0,347" fill="var(--green)"/>
    <polygon role="img" aria-label="Foto: Jugendspieler in grünem Trikot schießt den Ball auf dem Rasen" points="153,0 400,0 400,244 291,281" fill="url(#kidsPhoto)"/>
    <rect role="img" aria-label="Foto: Kinder beim Dribbeln im Training" x="182" y="299" width="97" height="73" fill="url(#drillPhoto)"/>
    <rect role="img" aria-label="Foto: Ballübung mit Hütchen auf dem Trainingsplatz" x="284" y="299" width="96" height="73" fill="url(#drillPhoto)"/>
    <polygon points="256,566 400,522 400,566" fill="var(--ink)"/>
  </svg>

  <div class="abs club-mark" style="left:34px;top:18px;width:131px;height:188px">
    <span class="club-mark__dot"></span>
    <span class="club-mark__name">Fussball Förderverein<br>Halmbeck e.V.</span>
  </div>

  <h1 class="abs headline">Unterstütze den<br>SpVg Halmbeck</h1>
  <p class="abs tagline">Gemeinsam für die<br>Zukunft unseres Vereins<br>und der Jugend!</p>

  <div class="abs info-box">
    <div class="info-box__col info-box__col--left">
      <h2>Über den<br>Förderverein:</h2>
      <p>Lorem ipsum dolor sit amet, consectetur adipiscing elit, sed do eiusmod tempor incididunt ut labore et dolore magna aliqua. Ut enim ad minim veniam, quis nostrud exercitation ullamco laboris nisi ut aliquip ex ea commodo consequat. Duis aute irure dolor in reprehenderit in voluptate velit esse cillum dolore eu fugiat nulla pariatur.</p>
    </div>
    <div class="info-box__col info-box__col--right">
      <h3>Vorteile für Vereine und Jugendliche:</h3>
      <p>Lorem ipsum dolor sit amet, consectetur adipiscing elit, sed do eiusmod tempor incididunt ut labore et dolore magna aliqua. Ut enim ad minim veniam, quis nostrud exercitation ullamco laboris nisi ut aliquip ex ea commodo consequat.</p>
      <p>Lorem ipsum dolor sit amet, consectetur adipiscing elit, sed do eiusmod tempor incididunt ut labore et dolore magna aliqua. Ut enim ad minim veniam, quis nostrud exercitation ullamco laboris nisi ut aliquip ex ea commodo consequat.</p>
    </div>
  </div>

  <p class="abs website">www.spvghalmbeck.de</p>
</section>

<!-- Rückseite -->
<section class="page page--back">
  <svg class="shapes" viewBox="0 0 400 566">
    <defs>
      <linearGradient id="stadiumPhoto" x1="0" y1="0" x2="0" y2="1">
        <stop offset="0" stop-color="#a9c9e8"/>
        <stop offset=".35" stop-color="#7f9aa8"/>
        <stop offset=".55" stop-color="#3d8a2e"/>
        <stop offset="1" stop-color="#2f7a22"/>
      </linearGradient>
    </defs>
    <polygon points="0,330 400,180 400,197 0,347" fill="var(--white)"/>
    <polygon role="img" aria-label="Foto: Fußballspieler in grünem Trikot nimmt im Stadion den Ball an" points="0,347 400,197 400,566 0,566" fill="url(#stadiumPhoto)"/>
    <polygon points="250,566 400,528 400,566" fill="var(--white)"/>
  </svg>

  <div class="abs back-section membership">
    <h2>Mitgliedschaft:</h2>
    <p>Lorem ipsum dolor sit amet, consectetur adipiscing elit, sed do eiusmod tempor incididunt ut labore et dolore magna aliqua. Ut enim ad minim veniam, quis nostrud exercitation ullamco laboris nisi ut aliquip ex ea commodo consequat. Duis aute irure dolor in reprehenderit in voluptate velit esse cillum dolore eu fugiat nulla pariatur.</p>
  </div>

  <div class="abs back-section donations">
    <h2>Spenden:</h2>
    <p>Möglichkeit der direkten Spende mit einem Hinweis auf steuerliche Vorteile (falls zutreffend). Möglicherweise auch die Angabe eines Spendenkontos.</p>
  </div>

  <div class="abs back-section benefits">
    <h2>Vorteile und der<br>Beitrag, der<br>benötigt wird.</h2>
    <p>Lorem ipsum dolor sit amet, consectetur adipiscing elit, sed do eiusmod tempor incididunt ut labore et dolore magna aliqua. Ut enim ad minim veniam, quis nostrud exercitation ullamco laboris nisi ut aliquip ex ea commodo consequat. Duis aute irure dolor in reprehenderit in voluptate velit esse cillum dolore eu fugiat nulla pariatur. Excepteur sint occaecat cupidatat non proident, sunt in culpa qui officia deserunt mollit anim id est laborum.</p>
  </div>

  <div class="abs back-section examples">
    <h2>Beispiele für die Verwendung von Mitteln:</h2>
    <p>Welche Projekte oder Anschaffungen wurden durch den Förderverein unterstützt (z.B. Trainingsmaterialien, Ausrüstung, Turniere, Jugendfahrten)?</p>
  </div>

  <div class="abs club-mark" style="left:34px;top:290px;width:131px;height:180px">
    <span class="club-mark__dot"></span>
    <span class="club-mark__name">Fussball Förderverein<br>Halmbeck e.V.</span>
  </div>

  <ul class="abs contact">
    <li><svg viewBox="0 0 10 10"><circle cx="5" cy="5" r="5" fill="#fff"/><path d="M3 2.3l1 .1.4 1.3-.6.5a4 4 0 0 0 1.9 1.9l.5-.6 1.3.4.1 1A1.2 1.2 0 0 1 6.4 8 4.8 4.8 0 0 1 2 3.6 1.2 1.2 0 0 1 3 2.3z" fill="var(--green)"/></svg>123-456-7890</li>
    <li><svg viewBox="0 0 10 10"><circle cx="5" cy="5" r="5" fill="#fff"/><rect x="2.4" y="3.2" width="5.2" height="3.6" fill="none" stroke="var(--green)" stroke-width=".8"/><path d="M2.6 3.4 5 5.2l2.4-1.8" fill="none" stroke="var(--green)" stroke-width=".8"/></svg>info@spvghalmbeck.de</li>
    <li><svg viewBox="0 0 10 10"><circle cx="5" cy="5" r="5" fill="#fff"/><circle cx="5" cy="5" r="2.8" fill="none" stroke="var(--green)" stroke-width=".7"/><ellipse cx="5" cy="5" rx="1.2" ry="2.8" fill="none" stroke="var(--green)" stroke-width=".7"/><path d="M2.2 5h5.6" stroke="var(--green)" stroke-width=".7"/></svg>spvghalmbeck.de</li>
  </ul>
</section>

</body>
</html>
```